Step and Repeat Backdrop for wedding reception photo booth

Would like to have a Step and Repeat Backdrop (8 foot high by 10 foot wide) that incorporates the wedding logo (attached) and the names Elena and Gavin. Background should be white, and wedding colors are burgundy and gold. Show me creativity :-) I have included some random samples.

```html
<!DOCTYPE html>
<html lang="en">
<head>
<meta charset="utf-8">
<title>Elena &amp; Gavin – Step and Repeat Backdrop</title>
<link rel="stylesheet" href="https://fonts.googleapis.com/css2?family=Cinzel:wght@500&family=Playfair+Display:wght@500&display=swap">
<style>
  :root {
    --gold: #a6813f;
    --gold-light: #c6a665;
    --white: #ffffff;
  }
  html, body {
    margin: 0;
    padding: 0;
    overflow: hidden;
  }
  body {
    width: 1200px;
    height: 1000px;
    background: var(--gold);
    position: relative;
  }
  .backdrop {
    position: absolute;
    left: 100px;
    top: 100px;
    width: 1000px;
    height: 800px;
    background: var(--white);
  }
  .repeat-grid {
    position: absolute;
    left: 34px;
    top: 31px;
    display: grid;
    grid-template-columns: repeat(8, 102px);
    grid-template-rows: repeat(12, 43px);
    column-gap: 16.3px;
    row-gap: 20.1px;
  }
  .tile {
    display: flex;
    align-items: center;
    justify-content: center;
    box-sizing: border-box;
  }
  .monogram {
    font-family: "Playfair Display", serif;
    font-weight: 500;
    font-size: 54px;
    line-height: 1;
    letter-spacing: -3px;
    color: var(--gold);
  }
  .names {
    background: var(--gold);
    flex-direction: column;
    font-family: "Cinzel", serif;
    font-weight: 500;
    font-size: 23px;
    line-height: 0.86;
    letter-spacing: 1px;
    color: var(--white);
    text-transform: uppercase;
  }
  .feature-panel {
    grid-column: 3 / 7;
    grid-row: 4 / 10;
    margin: 0 -2px;
    background: radial-gradient(ellipse at center, var(--gold-light) 0%, #b8955a 45%, var(--gold) 80%);
    display: flex;
    align-items: center;
    justify-content: center;
  }
  .feature-monogram {
    font-family: "Playfair Display", serif;
    font-weight: 500;
    font-size: 132px;
    line-height: 1;
    letter-spacing: -8px;
    color: var(--white);
  }
</style>
</head>
<body>
  <main class="backdrop">
    <div class="repeat-grid">
      <div class="feature-panel" role="img" aria-label="Gold panel with ornamental scrollwork above and below the couple's initials">
        <span class="feature-monogram">E&amp;G</span>
      </div>

      <!-- row 1 -->
      <div class="tile monogram">E&amp;G</div><div class="tile names"><span>Elena</span><span>Gavin</span></div>
      <div class="tile monogram">E&amp;G</div><div class="tile names"><span>Elena</span><span>Gavin</span></div>
      <div class="tile monogram">E&amp;G</div><div class="tile names"><span>Elena</span><span>Gavin</span></div>
      <div class="tile monogram">E&amp;G</div><div class="tile names"><span>Elena</span><span>Gavin</span></div>
      <!-- row 2 -->
      <div class="tile names"><span>Elena</span><span>Gavin</span></div><div class="tile monogram">E&amp;G</div>
      <div class="tile names"><span>Elena</span><span>Gavin</span></div><div class="tile monogram">E&amp;G</div>
      <div class="tile names"><span>Elena</span><span>Gavin</span></div><div class="tile monogram">E&amp;G</div>
      <div class="tile names"><span>Elena</span><span>Gavin</span></div><div class="tile monogram">E&amp;G</div>
      <!-- row 3 -->
      <div class="tile monogram">E&amp;G</div><div class="tile names"><span>Elena</span><span>Gavin</span></div>
      <div class="tile monogram">E&amp;G</div><div class="tile names"><span>Elena</span><span>Gavin</span></div>
      <div class="tile monogram">E&amp;G</div><div class="tile names"><span>Elena</span><span>Gavin</span></div>
      <div class="tile monogram">E&amp;G</div><div class="tile names"><span>Elena</span><span>Gavin</span></div>
      <!-- rows 4–9: side columns -->
      <div class="tile names"><span>Elena</span><span>Gavin</span></div><div class="tile monogram">E&amp;G</div>
      <div class="tile names"><span>Elena</span><span>Gavin</span></div><div class="tile monogram">E&amp;G</div>

      <div class="tile monogram">E&amp;G</div><div class="tile names"><span>Elena</span><span>Gavin</span></div>
      <div class="tile monogram">E&amp;G</div><div class="tile names"><span>Elena</span><span>Gavin</span></div>

      <div class="tile names"><span>Elena</span><span>Gavin</span></div><div class="tile monogram">E&amp;G</div>
      <div class="tile names"><span>Elena</span><span>Gavin</span></div><div class="tile monogram">E&amp;G</div>

      <div class="tile monogram">E&amp;G</div><div class="tile names"><span>Elena</span><span>Gavin</span></div>
      <div class="tile monogram">E&amp;G</div><div class="tile names"><span>Elena</span><span>Gavin</span></div>

      <div class="tile names"><span>Elena</span><span>Gavin</span></div><div class="tile monogram">E&amp;G</div>
      <div class="tile names"><span>Elena</span><span>Gavin</span></div><div class="tile monogram">E&amp;G</div>

      <div class="tile monogram">E&amp;G</div><div class="tile names"><span>Elena</span><span>Gavin</span></div>
      <div class="tile monogram">E&amp;G</div><div class="tile names"><span>Elena</span><span>Gavin</span></div>
      <!-- row 10 -->
      <div class="tile names"><span>Elena</span><span>Gavin</span></div><div class="tile monogram">E&amp;G</div>
      <div class="tile names"><span>Elena</span><span>Gavin</span></div><div class="tile monogram">E&amp;G</div>
      <div class="tile names"><span>Elena</span><span>Gavin</span></div><div class="tile monogram">E&amp;G</div>
      <div class="tile names"><span>Elena</span><span>Gavin</span></div><div class="tile monogram">E&amp;G</div>
      <!-- row 11 -->
      <div class="tile monogram">E&amp;G</div><div class="tile names"><span>Elena</span><span>Gavin</span></div>
      <div class="tile monogram">E&amp;G</div><div class="tile names"><span>Elena</span><span>Gavin</span></div>
      <div class="tile monogram">E&amp;G</div><div class="tile names"><span>Elena</span><span>Gavin</span></div>
      <div class="tile monogram">E&amp;G</div><div class="tile names"><span>Elena</span><span>Gavin</span></div>
      <!-- row 12 -->
      <div class="tile names"><span>Elena</span><span>Gavin</span></div><div class="tile monogram">E&amp;G</div>
      <div class="tile names"><span>Elena</span><span>Gavin</span></div><div class="tile monogram">E&amp;G</div>
      <div class="tile names"><span>Elena</span><span>Gavin</span></div><div class="tile monogram">E&amp;G</div>
      <div class="tile names"><span>Elena</span><span>Gavin</span></div><div class="tile monogram">E&amp;G</div>
    </div>
  </main>
</body>
</html>
```